An international recruitment business looking to attract new engineering and construction clients i

BK Worldwide is an international recruitment company with a wealth of experienced engineers, quantity surveyors and construction specialists appropriate to fill roles in the vastly growing Middle East. We need a new, attractive brochure design to send to new clients/companies so they will be interested in our recruitment company and our candidates. We have provided our company logo which we would like to feature, and we would like the theme to match this to some extent. We have also attached our current brochure which should be used for the general content and information. PLEASE NOTE: Ignore the appraisals on the penultimate page - I will provide new ones in a separate document. (Use the one with 5 appraisals, not 3!)
The final design should be modern and attractive and should feature some images of the Middle East including some impressive buildings and new railways (similar to our current ones).
Please also link our website
and use it for inspiration: http://www.bk-worldwide.co.uk
Updates
We would like the brochure to be A5 and landscape - although it will only be emailed to clients and not printed.
There is no limit on number of pages.
There seems to be a problem opening the appraisals document I attached.
The content of this document is:
BK Worldwide Appraisals
"I had the pleasure of working with BK Worldwide as a client and found them to be a great recruiter with in-depth rail knowledge, I had great results from them time after time. I found the team very trustworthy, professional and fun to work with. I would highly recommend BK Worldwide and will continue to use the company for all my future recruitment needs"
Tarek Olivastro, Dunemark Transit Company
“When looking to advance my career, I enquired with BK Worldwide about a senior position in the Middle East. I dealt specifically with Colin who I found very helpful. He informed me of all the job requirements, the background of the role, responsibilities and package. Colin was extremely diligent in moving the process forward and throughout kept in contact and abreast of the situation. In all it proved a great success and I am now happily placed in my new role. Even though Colin performed beyond the normal boundaries of his role he even now keeps in contact to make sure everything is ok and all parties happy and satisfied with the outcome. I wholeheartedly endorse Colin and BK Worldwide and will use them when I am next supplementing my team.”
Miles Thornbury, Head of Quantity Surveying, Vellum Gulf Design Partners (VGDP), Kuwait
BK Worldwide is a recruitment company that has an insatiable appetite for understanding the jobs, for which they recruit, and not only the jobs, but they also establish excellent rapport with the clients and candidates. They are always there when I need to fill positions in my organization quickly. They listen to what I need and always supply me with the resumes that I could review right away to start hiring who I needed - saving me time and effort. They are always able to supply me with the exact person that I need for the open position."
Nadia Faris, HR Consultant, Dunemark Transit
Target Market(s)
Professional clients in the Middle East
Industry/Entity Type
Construction
Colors
Designer to choose colors to be used in the design.
Look and feel

```html
<!DOCTYPE html>
<html lang="en">
<head>
<meta charset="utf-8">
<title>Expertise</title>
<link rel="stylesheet" href="https://fonts.googleapis.com/css2?family=Archivo+Narrow:wght@700&family=Noto+Serif:ital@1&family=Open+Sans&display=swap">
<style>
  :root {
    --backdrop: #e6eaeb;
    --navy-deep: #0a1848;
    --sky-top: #143a9a;
    --sky-glow: #6f9fe0;
    --accent-blue: #8cbcf6;
    --lead-blue: #8ab2ec;
    --body-text: #e8eefb;
  }
  html, body {
    margin: 0;
    width: 1200px;
    height: 1000px;
    overflow: hidden;
    background: var(--backdrop);
  }
  .brochure-page {
    position: absolute;
    left: 163px;
    top: 209px;
    width: 869px;
    height: 593px;
    background: var(--navy-deep);
    overflow: hidden;
  }
  .hero-photo {
    position: absolute;
    left: 0;
    top: 0;
    width: 869px;
    height: 330px;
    background: linear-gradient(180deg,
      var(--sky-top) 0%,
      #2c5bc0 30%,
      var(--sky-glow) 58%,
      #1c2a55 66%,
      #14245e 74%,
      #1a3478 84%,
      var(--navy-deep) 100%);
  }
  .section-title {
    position: absolute;
    left: 37px;
    top: 362px;
    margin: 0;
    font-family: "Archivo Narrow", "Arial Narrow", sans-serif;
    font-weight: 700;
    font-size: 46px;
    letter-spacing: 4px;
    line-height: 1;
    color: var(--accent-blue);
  }
  .line {
    display: block;
    white-space: nowrap;
    text-align: justify;
    text-align-last: justify;
  }
  .line--end { text-align-last: left; }
  .section-lead {
    position: absolute;
    left: 36px;
    top: 432px;
    width: 270px;
    margin: 0;
    font-family: "Noto Serif", Georgia, serif;
    font-style: italic;
    font-size: 14.5px;
    line-height: 19px;
    letter-spacing: 1px;
    color: var(--lead-blue);
  }
  .body-column {
    position: absolute;
    top: 337px;
    width: 240px;
    font-family: "Open Sans", Verdana, sans-serif;
    font-size: 11px;
    line-height: 15px;
    letter-spacing: 0.5px;
    color: var(--body-text);
  }
  .body-column p { margin: 0 0 15px; }
  .body-column--first { left: 336px; }
  .body-column--second { left: 603px; }
</style>
</head>
<body>
  <section class="brochure-page">
    <div class="hero-photo" role="img" aria-label="Photograph of a Middle East city skyline at dusk with skyscrapers, cranes and a waterfront reflecting the lights"></div>

    <h1 class="section-title">Expertise</h1>
    <p class="section-lead">
      <span class="line">As a consultancy we pride</span>
      <span class="line">ourselves in taking full</span>
      <span class="line">responsibility for providing</span>
      <span class="line">our clients with the very best</span>
      <span class="line">selection of professionals from</span>
      <span class="line line--end">across the globe.</span>
    </p>

    <div class="body-column body-column--first">
      <p>
        <span class="line">We currently recruit Construction &amp;</span>
        <span class="line">Engineering Professionals from the</span>
        <span class="line">UK, EU, Australia, New Zealand,</span>
        <span class="line">Canada &amp; the USA to work with our</span>
        <span class="line">prestigious clients across the Middle</span>
        <span class="line line--end">East.</span>
      </p>
      <p>
        <span class="line">Our company prides itself on taking</span>
        <span class="line">the time and effort involved in</span>
        <span class="line">understanding our clients, their</span>
        <span class="line">needs, their past and most</span>
        <span class="line">importantly the future of the</span>
        <span class="line">company and the direction it wishes</span>
      </p>
    </div>

    <div class="body-column body-column--second">
      <p>
        <span class="line">to take. This information, in turn</span>
        <span class="line">provides us with the specifications</span>
        <span class="line">we need to find the talent required</span>
        <span class="line line--end">for the future of your business.</span>
      </p>
      <p>
        <span class="line">We believe that research is a vital</span>
        <span class="line">part of keeping ahead. We therefore</span>
        <span class="line">dedicate part of our business to the</span>
        <span class="line">continued study of Recruitment</span>
        <span class="line">Trends, New Developments &amp;</span>
        <span class="line line--end">Economic Pressures that can have a</span>
        <span class="line">major effect on where to find and</span>
        <span class="line">source the best talent needed for</span>
        <span class="line line--end">you.</span>
      </p>
    </div>
  </section>
</body>
</html>
```